BRAVEN POWERLINE SERVICES needs a vibrant design for electrical contracting work.

I require a card design for my own electrical contracting business. I will be doing a lot of domestic and commercial work, including things such as repairs, maintenance, lighting, installations and various others. LED lighting and energy efficiency will be a big part of my business. I wish not to have childish pictures such as light bulbs in the design, but rather a smart and modern looking card which incorporates my logo colours and perhaps the same lighting strike within the faded background of the card.

Target Market(s)

Residential and Commercial property owners.

Industry/Entity Type

Electrical

Contact Information for Business Card

Dalen Voskic
EC40923
Phone Number: 0417 358 942
Email: dalen@bravenpowerline.com

Font styles to use
Serif
Sans Serif

Requirements
Must have
• My Logo and associated colours.
Nice to have
• Some form of shapes splitting the card into different colours related to the colours of my logo. Electric Blue, Silver/Grey and White.
Should not have
• Childish pictures and symbols such as light bulbs.

```html
<!DOCTYPE html>
<html lang="en">
<head>
<meta charset="utf-8">
<title>Braven Powerline Services – Business Card</title>
<link rel="stylesheet" href="https://fonts.googleapis.com/css2?family=Exo+2:wght@400;500;700&display=swap">
<style>
  :root {
    --electric-blue: #1717d9;
    --silver: #b9b9bd;
    --silver-dark: #8e8e93;
    --card-white: #f7f7f7;
    --page-bg: #e4e5ea;
    --text-light: #ffffff;
  }
  * { margin: 0; padding: 0; box-sizing: border-box; }
  html, body {
    width: 1200px;
    height: 840px;
    overflow: hidden;
    background: var(--page-bg);
    font-family: "Exo 2", sans-serif;
  }
  .canvas {
    position: relative;
    width: 1200px;
    height: 840px;
  }
  .business-card {
    position: absolute;
    left: 75px;
    top: 120px;
    width: 1050px;
    height: 600px;
    overflow: hidden;
    box-shadow: 0 10px 30px rgba(0, 0, 0, 0.18);
  }
  .card-shapes {
    position: absolute;
    inset: 0;
    width: 100%;
    height: 100%;
  }
  .brand {
    position: absolute;
    left: 60px;
    top: 215px;
    display: flex;
    align-items: center;
    gap: 16px;
  }
  .brand-dot {
    width: 64px;
    height: 64px;
    border-radius: 50%;
    background: var(--silver);
    flex: none;
  }
  .brand-name {
    color: var(--electric-blue);
    font-weight: 700;
    font-size: 25px;
    line-height: 1.1;
    letter-spacing: 0.5px;
    text-transform: uppercase;
    white-space: nowrap;
  }
  .contact {
    position: absolute;
    right: 48px;
    top: 62px;
    text-align: right;
    color: var(--text-light);
  }
  .contact-name {
    font-size: 30px;
    font-weight: 500;
    letter-spacing: 1px;
  }
  .contact-role {
    font-size: 20px;
    letter-spacing: 1px;
    margin-bottom: 62px;
  }
  .contact-address {
    font-size: 24px;
    line-height: 1.3;
    margin-bottom: 40px;
  }
  .contact-line {
    display: flex;
    justify-content: flex-end;
    align-items: center;
    gap: 14px;
    font-size: 24px;
    letter-spacing: 1px;
    height: 42px;
  }
  .contact-icon {
    width: 22px;
    height: 22px;
    flex: none;
  }
</style>
</head>
<body>
<main class="canvas">
  <section class="business-card">
    <svg class="card-shapes" viewBox="0 0 1050 600" preserveAspectRatio="none" aria-hidden="true">
      <defs>
        <linearGradient id="whiteFade" x1="0" y1="0" x2="1" y2="1">
          <stop offset="0" stop-color="#ffffff"/>
          <stop offset="0.6" stop-color="#f2f2f3"/>
          <stop offset="1" stop-color="#dcdcdf"/>
        </linearGradient>
        <linearGradient id="silverBand" x1="0" y1="0" x2="1" y2="0">
          <stop offset="0" stop-color="#a7a7ab"/>
          <stop offset="1" stop-color="#d2d2d6"/>
        </linearGradient>
      </defs>
      <rect class="card-base" width="1050" height="600" fill="url(#whiteFade)"/>
      <path class="silver-band" d="M655 0 L1050 0 L1050 600 L0 600 L0 478 C300 478 580 290 655 0 Z" fill="url(#silverBand)"/>
      <path class="blue-field" d="M690 0 L1050 0 L1050 600 L0 600 L0 505 C320 505 615 310 690 0 Z" fill="var(--electric-blue)"/>
    </svg>

    <div class="brand">
      <span class="brand-dot"></span>
      <span class="brand-name">Braven<br>Powerline Services</span>
    </div>

    <div class="contact">
      <p class="contact-name">TARIN OSWELD</p>
      <p class="contact-role">PRESIDENT</p>
      <p class="contact-address">Unit 14, 220 Corella St<br>Ashgrove</p>

      <p class="contact-line">0400 512 377
        <svg class="contact-icon" viewBox="0 0 24 24" aria-hidden="true"><path fill="#fff" d="M6.6 10.8a15 15 0 0 0 6.6 6.6l2.2-2.2a1 1 0 0 1 1-.25 11.4 11.4 0 0 0 3.6.6 1 1 0 0 1 1 1V20a1 1 0 0 1-1 1A17 17 0 0 1 3 4a1 1 0 0 1 1-1h3.5a1 1 0 0 1 1 1c0 1.25.2 2.45.6 3.6a1 1 0 0 1-.25 1z"/></svg>
      </p>
      <p class="contact-line">0400 512 377
        <svg class="contact-icon" viewBox="0 0 24 24" aria-hidden="true"><rect x="6" y="1.5" width="12" height="21" rx="2" fill="none" stroke="#fff" stroke-width="2"/><circle cx="12" cy="18.5" r="1.2" fill="#fff"/></svg>
      </p>
      <p class="contact-line">0400 512 377
        <svg class="contact-icon" viewBox="0 0 24 24" aria-hidden="true"><rect x="4" y="8" width="16" height="14" fill="#fff"/><rect x="7" y="2" width="10" height="6" fill="none" stroke="#fff" stroke-width="2"/><rect x="7" y="12" width="10" height="2" fill="var(--electric-blue)"/><rect x="7" y="16" width="10" height="2" fill="var(--electric-blue)"/></svg>
      </p>
      <p class="contact-line">info@bravenpowerline.com
        <svg class="contact-icon" viewBox="0 0 24 24" aria-hidden="true"><rect x="2" y="5" width="20" height="14" fill="#fff"/><path d="M2 5 L12 13 L22 5" fill="none" stroke="var(--electric-blue)" stroke-width="1.6"/></svg>
      </p>
      <p class="contact-line">www.bravenpowerline.com
        <svg class="contact-icon" viewBox="0 0 24 24" aria-hidden="true"><g fill="none" stroke="#fff" stroke-width="1.8"><circle cx="12" cy="12" r="10"/><ellipse cx="12" cy="12" rx="4.5" ry="10"/><path d="M2 12h20M4 7h16M4 17h16"/></g></svg>
      </p>
    </div>
  </section>
</main>
</body>
</html>
```